Pivots & Treads .com

This website is simple!!!
Landing page background image should capture the customers attention!!! We will provide a image as a example of what we like. The purpose for this website is to provide customers with a clean easy way to request a quote for industrial casters and wheels by OEM’s as well as maintenance departments worldwide. Please see if you can follow our thought process below.
Customer comes to website, they are invited to Request a Quote by providing us with Manufacturer Name, Manufacturers Part # and quantity needed.
If this is not known the customer will complete will WP conversation format form answering about 10 questions
Or
Look up the part number in one of the 8 to 12 catalogs located in the Flippin Book format on our catalog page, or equal plug in .
When the client request a quote a account page will pop up request The following:
Clients first and last name
Email address
And optional questions
Company name and best contact number.
Once this is complete customer will hit SUBMIT.
The customers request will be in system. A email will be sent to Customer service notifying us the Quote Request has been made.
We will then build a quote for the customer with a good, better and best options. Customers Request a Quote submission may have more than one caster or wheel requested at a time, so website must allow this.
When the customer comes back into website there email address will come up as the account name and request a password be made for them. This will allow them to store quotes in their account for future needs. If quote is older than 30 day the system will trigger a button at the bottom of the quote for resubmit Request for updated quote.
Once customer reviews quote the quote can be Converted to order within the website.
Once Converted the system will send us a email and order will be processed.
We will need a Chat program that will text to CS the questions.
You will need to have high quality graphic design skills on your team.
We have found 2 plugins that would work nicely with our new website Flippin books to showcase our catalogs for customers to research and WPForms conversation forms to complete request for quote form.
Just Ideas:
Very very ghosted caster blueprint in white background but very very ghosted or the icon just idea
We have never had a font used we like
Grayscale every except for rubber on wheels and logo icon
Website should have hamburger menu on left
Website should hav responsive deign
Account head on right side
Has anyone read the brief from top to bottom and the updates, I’m seeing a lot of duplicates of the website I posted in images I want a clean website With lite backgrand with the poly being definite colors on each wheel I added a green yellow and red image has anyone looked at that Just a question?
Went on vacation/holiday

```html
<!DOCTYPE html>
<html lang="en">
<head>
<meta charset="utf-8">
<title>Pivots &amp; Treads .com</title>
<link rel="stylesheet" href="https://fonts.googleapis.com/css2?family=Montserrat:wght@400;500;600;700;800&display=swap">
<style>
:root{
  --navy:#2e4593;
  --navy-deep:#22357a;
  --cyan:#14b5f0;
  --grey-band:#ededed;
  --ink:#1d1d1f;
  --muted:#333;
  --white:#fff;
}
*{box-sizing:border-box;margin:0;padding:0}
html,body{width:684px;height:1200px;overflow:hidden;background:#fff}
body{font-family:'Montserrat',sans-serif;color:var(--ink)}
.board{position:absolute;left:2px;top:0;width:1450px;height:2560px;transform:scale(0.46875);transform-origin:0 0}
.page{position:absolute;top:90px;width:668px;height:2375px;overflow:hidden;background:#fff}
.page--home{left:37px}
.page--quote{left:745px}
.abs{position:absolute}

/* hero */
.hero-photo{left:0;top:0;width:668px;height:520px;background:
  radial-gradient(ellipse at 30% 55%,rgba(190,120,70,.55),transparent 55%),
  radial-gradient(ellipse at 80% 40%,rgba(120,130,140,.45),transparent 60%),
  linear-gradient(180deg,#0e0f12 0%,#2b2a2a 45%,#3b3128 100%)}
.hero-curve{left:0;top:380px;width:668px;height:140px}
.menu-btn{left:96px;top:18px;width:38px;height:38px;border:2.5px solid var(--navy);border-radius:50%}
.menu-btn span{position:absolute;left:10px;width:14px;height:2.5px;background:var(--navy);border-radius:2px}
.brand{left:184px;top:20px;width:300px;text-align:center;color:var(--white)}
.brand-mark{width:44px;height:44px;border-radius:50%;border:5px solid var(--white);margin:0 auto 10px}
.brand-name{font-size:14px;font-weight:700;letter-spacing:.3px}
.brand-name small{font-size:14px;font-weight:700}
.login{left:487px;top:27px;width:85px;height:29px;border-radius:15px;background:var(--navy);color:#fff;font-size:11px;font-weight:700;display:flex;align-items:center;justify-content:center;gap:6px}
.login svg{width:14px;height:14px}
.hero-title{left:60px;top:255px;color:#fff;font-size:21px;font-weight:700}
.hero-title small{font-size:21px;font-weight:500}
.hero-tag{left:61px;top:288px;width:290px;color:#fff;font-size:10.5px;font-weight:600;line-height:1.2}

.request-box{left:380px;top:112px;width:192px;height:233px;background:var(--navy);border:2px solid #fff}
.request-box h2{color:#fff;font-size:13px;font-weight:700;text-align:center;line-height:1.5;margin-top:18px}
.select{position:absolute;left:16px;width:158px;height:25px;background:#fff;border-radius:3px;font-size:7px;color:var(--navy);padding:0 9px;display:flex;align-items:center;justify-content:space-between}
.select::after{content:"";border-left:4px solid transparent;border-right:4px solid transparent;border-top:5px solid #111}
.btn-request{position:absolute;left:16px;top:177px;width:158px;height:28px;background:var(--cyan);border:2px solid #fff;border-radius:4px;color:#fff;font-size:9px;font-weight:700;display:flex;align-items:center;justify-content:center}

/* headings */
.section-title{width:668px;text-align:center;color:var(--navy);font-size:21px;font-weight:700;letter-spacing:.3px}
.pill{position:absolute;height:28px;border-radius:14px;color:#fff;font-size:9px;font-weight:700;display:flex;align-items:center;justify-content:center}
.pill--navy{background:var(--navy)}
.pill--cyan{background:var(--cyan)}

/* steps */
.step{position:absolute;top:578px;width:170px}
.step-num{position:absolute;left:0;top:0;font-size:36px;font-weight:800;color:var(--navy);line-height:1;letter-spacing:-1px;-webkit-mask:linear-gradient(#000 55%,rgba(0,0,0,.25));mask:linear-gradient(#000 55%,rgba(0,0,0,.25))}
.step-title{position:absolute;left:52px;top:5px;font-size:12px;font-weight:600;color:var(--navy);line-height:1.1}
.step-text{position:absolute;left:52px;top:42px;width:115px;font-size:8.5px;color:var(--muted);line-height:1.3}

/* products */
.band{left:0;width:668px;background:var(--grey-band)}
.card{position:absolute;top:887px;width:149px;height:179px;background:#fff;box-shadow:0 1px 4px rgba(0,0,0,.15);text-align:center}
.card-photo{margin:14px auto 0;width:130px;height:86px;border-radius:4px}
.card h3{font-size:10.5px;font-weight:700;margin-top:16px}
.card p{font-size:5.5px;line-height:1.4;padding:4px 12px 0;color:#222}
.arrow{position:absolute;top:966px;width:31px;height:31px;border:2px solid var(--navy);border-radius:50%}
.arrow svg{width:27px;height:27px}

/* about */
.about-title{left:97px;top:1222px;color:var(--navy);font-size:21px;font-weight:700}
.about-text{left:97px;top:1262px;width:244px;font-size:10.5px;line-height:1.45;color:var(--ink)}
.about-photo{left:360px;top:1222px;width:224px;height:228px;background:
  radial-gradient(circle at 55% 75%,rgba(255,160,40,.8),transparent 35%),
  linear-gradient(160deg,#4a4d52,#1c1d20 60%,#3a2a18)}

/* quality */
.quality-photo{border-radius:50%;border:3px solid #fff}
.quality-title{left:342px;top:1550px;color:var(--navy);font-size:21px;font-weight:700;line-height:.97}
.quality-text{left:344px;top:1625px;width:235px;font-size:10.5px;line-height:1.45}

/* testimonials */
.avatar{position:absolute;top:1935px;width:62px;height:62px;border-radius:50%}
.quote{position:absolute;top:2012px;width:150px;font-size:9.5px;font-style:italic;text-align:center;line-height:1.3}
.person{position:absolute;top:2065px;width:150px;font-size:10px;font-weight:700;color:var(--navy);text-align:center}

/* footer */
.footer-wave{left:0;top:2030px;width:668px;height:345px}
.foot-brand{left:90px;top:2175px;width:160px;text-align:center;color:#fff}
.foot-mark{width:38px;height:38px;border-radius:50%;border:4px solid #fff;margin:0 auto 10px}
.foot-brand .name{font-size:10px;font-weight:700;letter-spacing:1.2px}
.foot-brand p{font-size:8px;line-height:1.2;margin-top:14px}
.foot-head{top:2183px;color:#fff;font-size:11px;font-weight:700}
.contact{position:absolute;left:289px;display:flex;gap:10px;color:#fff;font-size:9.5px;line-height:1.15}
.contact svg{width:10px;height:10px;flex:none;margin-top:1px}
.links{left:471px;top:2210px;color:#fff;font-size:8.5px;line-height:1.8;list-style:none}
.foot-rule{left:0;top:2334px;width:668px;height:1px;background:rgba(255,255,255,.35)}
.copy{left:0;top:2350px;width:668px;text-align:center;color:#fff;font-size:7.5px}

/* quote overlay */
.dim{left:0;top:0;width:668px;height:2375px;background:rgba(0,0,0,.7)}
.modal{left:120px;top:113px;width:428px;height:238px;background:var(--navy);border:2px solid #fff}
.field{position:absolute;left:26px;width:157px;height:26px;background:#fff;border-radius:3px;font-size:9px;color:#222;padding:0 10px;display:flex;align-items:center}
.questions{position:absolute;left:190px;top:38px;width:219px;height:162px;background:#fff;border-radius:4px;font-size:9px;padding:12px 10px}
.submit{position:absolute;left:326px;top:172px;width:81px;height:26px;background:var(--cyan);border:2px solid #fff;border-radius:4px;color:#fff;font-size:9px;font-weight:700;display:flex;align-items:center;justify-content:center}
.close{left:535px;top:99px;width:27px;height:27px;border-radius:50%;background:#fff;color:var(--navy);font-size:11px;font-weight:700;display:flex;align-items:center;justify-content:center}
</style>
</head>
<body>
<div class="board">

<!-- ========== HOME ========== -->
<section class="page page--home">
  <div class="abs hero-photo" role="img" aria-label="Worker in hard hat and safety glasses operating an industrial lathe"></div>
  <svg class="abs hero-curve" viewBox="0 0 668 140" preserveAspectRatio="none">
    <path d="M0 122 C120 70 260 20 380 18 C500 16 610 70 668 128 L668 140 L0 140 Z" fill="#fff"/>
    <path d="M170 55 C260 25 330 18 380 18 C500 16 610 70 668 128" fill="none" stroke="var(--cyan)" stroke-width="6"/>
  </svg>

  <div class="abs menu-btn"><span style="top:11px"></span><span style="top:16.5px"></span><span style="top:22px"></span></div>
  <div class="abs brand"><div class="brand-mark"></div><div class="brand-name">PIVOTS &amp; TREADS <small>.com</small></div></div>
  <div class="abs login"><svg viewBox="0 0 16 16"><circle cx="8" cy="5" r="3.5" fill="#fff"/><path d="M1.5 15c0-4 3-6 6.5-6s6.5 2 6.5 6z" fill="#fff"/></svg>LOG IN</div>

  <div class="abs hero-title">PIVOTS &amp; TREADS <small>.com</small></div>
  <p class="abs hero-tag">Lorem ipsum dolor sit amet, consectetur adipiscing elit, sed do eiusmod tempor incididunt ut la</p>

  <div class="abs request-box">
    <h2>REQUEST A<br>PIVOTS &amp; TREADS</h2>
    <div class="select" style="top:70px">Manufacturer Name</div>
    <div class="select" style="top:105px">Manufacturer Part</div>
    <div class="select" style="top:140px">Quantity</div>
    <div class="btn-request">REQUEST</div>
  </div>

  <h2 class="abs section-title" style="top:493px">HOW IT WORKS</h2>
  <svg class="abs" style="left:125px;top:538px" width="170" height="20" viewBox="0 0 170 20"><path d="M2 18 C50 0 120 0 168 18" fill="none" stroke="var(--cyan)" stroke-width="3.5"/></svg>
  <svg class="abs" style="left:333px;top:668px" width="170" height="20" viewBox="0 0 170 20"><path d="M2 2 C50 20 120 20 168 2" fill="none" stroke="var(--cyan)" stroke-width="3.5"/></svg>

  <div class="step" style="left:72px"><div class="step-num">01</div><div class="step-title">Request a<br>Quote</div><p class="step-text">Lorem ipsum dolor sit amet, consectetur adipis cing elit, sed aliqua.</p></div>
  <div class="step" style="left:243px"><div class="step-num">02</div><div class="step-title">Receive<br>a Quote</div><p class="step-text">Lorem ipsum dolor sit amet, consectetur adipis cing elit, sed aliqua.</p></div>
  <div class="step" style="left:424px"><div class="step-num">03</div><div class="step-title">Convert a<br>Quote to Order</div><p class="step-text">Lorem ipsum dolor sit amet, consectetur adipis cing elit, sed aliqua.</p></div>

  <div class="pill pill--navy" style="left:218px;top:717px;width:132px">REQUEST A QUOTE</div>
  <div class="pill pill--cyan" style="left:360px;top:717px;width:74px">CATALOG</div>

  <div class="abs band" style="top:796px;height:370px"></div>
  <h2 class="abs section-title" style="top:837px">OUR PRODUCTS</h2>
  <div class="arrow" style="left:29px"><svg viewBox="0 0 27 27"><path d="M15.5 8 L10 13.5 L15.5 19" fill="none" stroke="var(--navy)" stroke-width="2"/></svg></div>
  <div class="arrow" style="left:603px"><svg viewBox="0 0 27 27"><path d="M11.5 8 L17 13.5 L11.5 19" fill="none" stroke="var(--navy)" stroke-width="2"/></svg></div>
  <div class="card" style="left:97px"><div class="card-photo" role="img" aria-label="Two blue swivel casters with red brakes" style="background:linear-gradient(135deg,#c7ccd6,#2f5bbf 55%,#1b3b8a)"></div><h3>PRODUCT NAME</h3><p>Lorem ipsum dolor sit amet, consectetur adipiscing elit, sed do eiusmod tempor incididunt ut labore et dolore magna aliqua.</p></div>
  <div class="card" style="left:257px"><div class="card-photo" role="img" aria-label="Three assorted swivel casters with red, black and grey wheels" style="background:linear-gradient(135deg,#9a9da3,#c23a54 50%,#3b3c40)"></div><h3>PRODUCT NAME</h3><p>Lorem ipsum dolor sit amet, consectetur adipiscing elit, sed do eiusmod tempor incididunt ut labore et dolore magna aliqua.</p></div>
  <div class="card" style="left:420px"><div class="card-photo" role="img" aria-label="Black rubber wheel" style="background:radial-gradient(circle,#6a6a6a 0 15%,#1b1b1b 45%,#fff 48%)"></div><h3>PRODUCT NAME</h3><p>Lorem ipsum dolor sit amet, consectetur adipiscing elit, sed do eiusmod tempor incididunt ut labore et dolore magna aliqua.</p></div>
  <div class="pill pill--navy" style="left:268px;top:1090px;width:132px">VIEW ALL PRODUCTS</div>

  <h2 class="abs about-title">ABOUT US</h2>
  <p class="abs about-text">Lorem ipsum dolor sit amet, consectetur adip scing elit, sed do eiusmod tempor incididunt ut labore et dolore magna aliqua. Ut enim ad minim veniam, quis nostrud exercitation ulla mco laboris nisi ut aliquip ex ea commodo consequat. Duis aute irure dolor in reprehe nderit in voluptate velit esse cillum dolore eu fugiat nulla pariatur. Excepteur sint occaecat cupidatat non proident, sunt</p>
  <div class="pill pill--navy" style="left:97px;top:1410px;width:101px">RAED MORE</div>
  <div class="abs about-photo" role="img" aria-label="Angle grinder throwing sparks in a metal workshop"></div>

  <div class="abs band" style="top:1503px;height:331px"></div>
  <div class="abs quality-photo" role="img" aria-label="Warehouse aisle with pallet jack and stacked boxes" style="left:95px;top:1560px;width:190px;height:190px;background:linear-gradient(160deg,#dfe3e8,#8a7a68 60%,#4a3a2c)"></div>
  <div class="abs quality-photo" role="img" aria-label="Warehouse worker in overalls pulling a pallet jack" style="left:176px;top:1640px;width:144px;height:144px;background:linear-gradient(160deg,#7a5a3a,#2e4a8c 65%,#1a2a50)"></div>
  <h2 class="abs quality-title">HIGHEST QUALITY<br>METAL INDUSTRIAL<br>CASTERS</h2>
  <p class="abs quality-text">Lorem ipsum dolor sit amet, consectetur adip iscing elit, sed do eiusmod tempor incididunt ut labore et dolore magna aliqua. Ut enim ad minim veniam, quis nostrud exercitation ullamco laboris nisi ut aliquip ex ea commodo consequat. Duis aute irure dolor in reprehenderit in voluptate velit esse cillum dolore eu fugiat nulla pariatur.</p>
  <div class="pill pill--navy" style="left:343px;top:1758px;width:132px">REQUEST A QUOTE</div>

  <h2 class="abs section-title" style="top:1869px">TESTIMONIAL</h2>
  <svg class="abs footer-wave" viewBox="0 0 668 345" preserveAspectRatio="none">
    <path d="M0 0 C150 115 400 135 668 0 L668 345 L0 345 Z" fill="var(--navy)"/>
    <path d="M0 10 C110 95 260 120 470 88" fill="none" stroke="var(--cyan)" stroke-width="6"/>
  </svg>
  <div class="avatar" role="img" aria-label="Customer portrait" style="left:136px;background:linear-gradient(#c9ccd2,#3a3f4a)"></div>
  <div class="avatar" role="img" aria-label="Customer portrait" style="left:302px;background:linear-gradient(#e6e9ee,#2f6fd0);border:2px solid var(--navy)"></div>
  <div class="avatar" role="img" aria-label="Customer portrait" style="left:470px;background:linear-gradient(#f0f0f0,#3b2a22)"></div>
  <p class="quote" style="left:93px">"Lorem ipsum dolor sit amet, consectetur sed do &nbsp;incididunt ut labore et laborum."</p>
  <p class="quote" style="left:259px">"Lorem ipsum dolor sit amet, consectetur sed do &nbsp;incididunt ut labore et laborum."</p>
  <p class="quote" style="left:426px">"Lorem ipsum dolor sit amet, consectetur sed do &nbsp;incididunt ut labore et laborum."</p>
  <div class="person" style="left:93px">NOLAN</div>
  <div class="person" style="left:259px">JONAH WADE</div>
  <div class="person" style="left:426px">CARINA</div>

  <div class="abs foot-brand"><div class="foot-mark"></div><div class="name">PIVOTS &amp; TREADS.com</div><p>Lorem ipsum dolor sit amet, conse ctetur adipiscing elit, sed do eiusm od tempor incididunt ut labor</p></div>
  <div class="abs foot-head" style="left:283px">CONTACT US</div>
  <div class="contact" style="top:2213px"><svg viewBox="0 0 10 10"><path d="M5 0a3.5 3.5 0 0 0-3.5 3.5C1.5 6 5 10 5 10s3.5-4 3.5-6.5A3.5 3.5 0 0 0 5 0z" fill="#fff"/><circle cx="5" cy="3.5" r="1.3" fill="var(--navy)"/></svg><span>Lorem ipsum dolor sit<br>amet, aliqua.</span></div>
  <div class="contact" style="top:2253px"><svg viewBox="0 0 10 10"><path d="M2 0.5l1.8 2.2-1 1.2c.7 1.5 1.8 2.6 3.3 3.3l1.2-1 2.2 1.8-.9 1.5C4.5 9.2.8 5.5.5 1.4z" fill="#fff"/></svg><span>+1 (555)014-2290</span></div>
  <div class="contact" style="top:2283px"><svg viewBox="0 0 10 10"><rect x="0.5" y="2" width="9" height="6" fill="#fff"/><path d="M0.5 2l4.5 3.5L9.5 2" fill="none" stroke="var(--navy)" stroke-width="0.8"/></svg><span>hello@pivotstreads.com</span></div>
  <div class="abs foot-head" style="left:470px">Links</div>
  <ul class="abs links"><li>Home</li><li>About</li><li>Shop</li><li>Products</li><li>My Account</li><li>Shipping &amp; Delivery</li><li>FAQ's</li></ul>
  <div class="abs foot-rule"></div>
  <p class="abs copy">Copyrights © 2022 company name I All Rights Reversed</p>
</section>

<!-- ========== QUOTE REQUEST OPEN ========== -->
<section class="page page--quote">
  <div class="abs hero-photo" role="img" aria-label="Worker in hard hat and safety glasses operating an industrial lathe"></div>
  <svg class="abs hero-curve" viewBox="0 0 668 140" preserveAspectRatio="none">
    <path d="M0 122 C120 70 260 20 380 18 C500 16 610 70 668 128 L668 140 L0 140 Z" fill="#fff"/>
    <path d="M170 55 C260 25 330 18 380 18 C500 16 610 70 668 128" fill="none" stroke="var(--cyan)" stroke-width="6"/>
  </svg>
  <div class="abs menu-btn"><span style="top:11px"></span><span style="top:16.5px"></span><span style="top:22px"></span></div>
  <div class="abs brand"><div class="brand-mark"></div><div class="brand-name">PIVOTS &amp; TREADS <small>.com</small></div></div>
  <div class="abs login"><svg viewBox="0 0 16 16"><circle cx="8" cy="5" r="3.5" fill="#fff"/><path d="M1.5 15c0-4 3-6 6.5-6s6.5 2 6.5 6z" fill="#fff"/></svg>LOG IN</div>
  <div class="abs hero-title">PIVOTS &amp; TREADS <small>.com</small></div>
  <p class="abs hero-tag">Lorem ipsum dolor sit amet, consectetur adipiscing elit, sed do eiusmod tempor incididunt ut la</p>
  <div class="abs request-box">
    <h2>REQUEST A<br>PIVOTS &amp; TREADS</h2>
    <div class="select" style="top:70px">Manufacturer Name</div>
    <div class="select" style="top:105px">Manufacturer Part</div>
    <div class="select" style="top:140px">Quantity</div>
    <div class="btn-request">REQUEST</div>
  </div>

  <h2 class="abs section-title" style="top:493px">HOW IT WORKS</h2>
  <svg class="abs" style="left:125px;top:538px" width="170" height="20" viewBox="0 0 170 20"><path d="M2 18 C50 0 120 0 168 18" fill="none" stroke="var(--cyan)" stroke-width="3.5"/></svg>
  <svg class="abs" style="left:333px;top:668px" width="170" height="20" viewBox="0 0 170 20"><path d="M2 2 C50 20 120 20 168 2" fill="none" stroke="var(--cyan)" stroke-width="3.5"/></svg>
  <div class="step" style="left:72px"><div class="step-num">01</div><div class="step-title">Request a<br>Quote</div><p class="step-text">Lorem ipsum dolor sit amet, consectetur adipis cing elit, sed aliqua.</p></div>
  <div class="step" style="left:243px"><div class="step-num">02</div><div class="step-title">Receive<br>a Quote</div><p class="step-text">Lorem ipsum dolor sit amet, consectetur adipis cing elit, sed aliqua.</p></div>
  <div class="step" style="left:424px"><div class="step-num">03</div><div class="step-title">Convert a<br>Quote to Order</div><p class="step-text">Lorem ipsum dolor sit amet, consectetur adipis cing elit, sed aliqua.</p></div>
  <div class="pill pill--navy" style="left:218px;top:717px;width:132px">REQUEST A QUOTE</div>
  <div class="pill pill--cyan" style="left:360px;top:717px;width:74px">CATALOG</div>

  <div class="abs band" style="top:796px;height:370px"></div>
  <h2 class="abs section-title" style="top:837px">OUR PRODUCTS</h2>
  <div class="arrow" style="left:29px"><svg viewBox="0 0 27 27"><path d="M15.5 8 L10 13.5 L15.5 19" fill="none" stroke="var(--navy)" stroke-width="2"/></svg></div>
  <div class="arrow" style="left:603px"><svg viewBox="0 0 27 27"><path d="M11.5 8 L17 13.5 L11.5 19" fill="none" stroke="var(--navy)" stroke-width="2"/></svg></div>
  <div class="card" style="left:97px"><div class="card-photo" role="img" aria-label="Two blue swivel casters with red brakes" style="background:linear-gradient(135deg,#c7ccd6,#2f5bbf 55%,#1b3b8a)"></div><h3>PRODUCT NAME</h3><p>Lorem ipsum dolor sit amet, consectetur adipiscing elit, sed do eiusmod tempor incididunt ut labore et dolore magna aliqua.</p></div>
  <div class="card" style="left:257px"><div class="card-photo" role="img" aria-label="Three assorted swivel casters with red, black and grey wheels" style="background:linear-gradient(135deg,#9a9da3,#c23a54 50%,#3b3c40)"></div><h3>PRODUCT NAME</h3><p>Lorem ipsum dolor sit amet, consectetur adipiscing elit, sed do eiusmod tempor incididunt ut labore et dolore magna aliqua.</p></div>
  <div class="card" style="left:420px"><div class="card-photo" role="img" aria-label="Black rubber wheel" style="background:radial-gradient(circle,#6a6a6a 0 15%,#1b1b1b 45%,#fff 48%)"></div><h3>PRODUCT NAME</h3><p>Lorem ipsum dolor sit amet, consectetur adipiscing elit, sed do eiusmod tempor incididunt ut labore et dolore magna aliqua.</p></div>
  <div class="pill pill--navy" style="left:268px;top:1090px;width:132px">VIEW ALL PRODUCTS</div>

  <h2 class="abs about-title">ABOUT US</h2>
  <p class="abs about-text">Lorem ipsum dolor sit amet, consectetur adip scing elit, sed do eiusmod tempor incididunt ut labore et dolore magna aliqua. Ut enim ad minim veniam, quis nostrud exercitation ulla mco laboris nisi ut aliquip ex ea commodo consequat. Duis aute irure dolor in reprehe nderit in voluptate velit esse cillum dolore eu fugiat nulla pariatur. Excepteur sint occaecat cupidatat non proident, sunt</p>
  <div class="pill pill--navy" style="left:97px;top:1410px;width:101px">RAED MORE</div>
  <div class="abs about-photo" role="img" aria-label="Angle grinder throwing sparks in a metal workshop"></div>

  <div class="abs band" style="top:1503px;height:331px"></div>
  <div class="abs quality-photo" role="img" aria-label="Warehouse aisle with pallet jack and stacked boxes" style="left:95px;top:1560px;width:190px;height:190px;background:linear-gradient(160deg,#dfe3e8,#8a7a68 60%,#4a3a2c)"></div>
  <div class="abs quality-photo" role="img" aria-label="Warehouse worker in overalls pulling a pallet jack" style="left:176px;top:1640px;width:144px;height:144px;background:linear-gradient(160deg,#7a5a3a,#2e4a8c 65%,#1a2a50)"></div>
  <h2 class="abs quality-title">HIGHEST QUALITY<br>METAL INDUSTRIAL<br>CASTERS</h2>
  <p class="abs quality-text">Lorem ipsum dolor sit amet, consectetur adip iscing elit, sed do eiusmod tempor incididunt ut labore et dolore magna aliqua. Ut enim ad minim veniam, quis nostrud exercitation ullamco laboris nisi ut aliquip ex ea commodo consequat. Duis aute irure dolor in reprehenderit in voluptate velit esse cillum dolore eu fugiat nulla pariatur.</p>
  <div class="pill pill--navy" style="left:343px;top:1758px;width:132px">REQUEST A QUOTE</div>

  <h2 class="abs section-title" style="top:1869px">TESTIMONIAL</h2>
  <svg class="abs footer-wave" viewBox="0 0 668 345" preserveAspectRatio="none">
    <path d="M0 0 C150 115 400 135 668 0 L668 345 L0 345 Z" fill="var(--navy)"/>
    <path d="M0 10 C110 95 260 120 470 88" fill="none" stroke="var(--cyan)" stroke-width="6"/>
  </svg>
  <div class="avatar" role="img" aria-label="Customer portrait" style="left:136px;background:linear-gradient(#c9ccd2,#3a3f4a)"></div>
  <div class="avatar" role="img" aria-label="Customer portrait" style="left:302px;background:linear-gradient(#e6e9ee,#2f6fd0);border:2px solid var(--navy)"></div>
  <div class="avatar" role="img" aria-label="Customer portrait" style="left:470px;background:linear-gradient(#f0f0f0,#3b2a22)"></div>
  <p class="quote" style="left:93px">"Lorem ipsum dolor sit amet, consectetur sed do &nbsp;incididunt ut labore et laborum."</p>
  <p class="quote" style="left:259px">"Lorem ipsum dolor sit amet, consectetur sed do &nbsp;incididunt ut labore et laborum."</p>
  <p class="quote" style="left:426px">"Lorem ipsum dolor sit amet, consectetur sed do &nbsp;incididunt ut labore et laborum."</p>
  <div class="person" style="left:93px">NOLAN</div>
  <div class="person" style="left:259px">JONAH WADE</div>
  <div class="person" style="left:426px">CARINA</div>

  <div class="abs foot-brand"><div class="foot-mark"></div><div class="name">PIVOTS &amp; TREADS.com</div><p>Lorem ipsum dolor sit amet, conse ctetur adipiscing elit, sed do eiusm od tempor incididunt ut labor</p></div>
  <div class="abs foot-head" style="left:283px">CONTACT US</div>
  <div class="contact" style="top:2213px"><svg viewBox="0 0 10 10"><path d="M5 0a3.5 3.5 0 0 0-3.5 3.5C1.5 6 5 10 5 10s3.5-4 3.5-6.5A3.5 3.5 0 0 0 5 0z" fill="#fff"/><circle cx="5" cy="3.5" r="1.3" fill="var(--navy)"/></svg><span>Lorem ipsum dolor sit<br>amet, aliqua.</span></div>
  <div class="contact" style="top:2253px"><svg viewBox="0 0 10 10"><path d="M2 0.5l1.8 2.2-1 1.2c.7 1.5 1.8 2.6 3.3 3.3l1.2-1 2.2 1.8-.9 1.5C4.5 9.2.8 5.5.5 1.4z" fill="#fff"/></svg><span>+1 (555)014-2290</span></div>
  <div class="contact" style="top:2283px"><svg viewBox="0 0 10 10"><rect x="0.5" y="2" width="9" height="6" fill="#fff"/><path d="M0.5 2l4.5 3.5L9.5 2" fill="none" stroke="var(--navy)" stroke-width="0.8"/></svg><span>hello@pivotstreads.com</span></div>
  <div class="abs foot-head" style="left:470px">Links</div>
  <ul class="abs links"><li>Home</li><li>About</li><li>Shop</li><li>Products</li><li>My Account</li><li>Shipping &amp; Delivery</li><li>FAQ's</li></ul>
  <div class="abs foot-rule"></div>
  <p class="abs copy">Copyrights © 2022 company name I All Rights Reversed</p>

  <div class="abs dim"></div>
  <div class="abs modal">
    <div class="field" style="top:38px">First name</div>
    <div class="field" style="top:72px">Last name</div>
    <div class="field" style="top:105px">Email Address</div>
    <div class="field" style="top:139px">Company name</div>
    <div class="field" style="top:173px">Contact number</div>
    <div class="questions">Optional questions</div>
    <div class="submit">SUBMIT</div>
  </div>
  <div class="abs close">x</div>
</section>

</div>
</body>
</html>
```